B2B Consulting firm needs a re-fresh of its process diagrams

We are a commercial real estate consulting firm. Think: I wonder who Kovarelli uses when they have to build a new plant and sell the old one? That's us! We have created diagrams that we use to demonstrate to our clients the process of the project that they are about to go through. That is our "frontstage" diagram. We also have a "backstage" diagram that we use to train employees and to ensure that we do not make a stupid mistake! Here is a video showing you a little about what we are wanting https://view.clipframely.com/v/QpRtWz7YbLm2KdFs8JxV

Target Market(s)

B2B - C-suite and business leaders

Industry/Entity Type

Commercial Real Estate

Font styles to use
Sans Serif

Colors
0094D4
00A9DD
6FCCEA
C7EBF8
E9F6FB
EB3D1F
EC4F4E
F09395
F8D3D4
FCEDEE

Requirements
Must have
• Think of it as a infographic - clean and modern
Nice to have
• I would suggest that you look at the infographics that are used by Talmont Trade Quarterly, Prewitt, RDVF and other professional services firms/publications.

```html
<!DOCTYPE html>
<html lang="en">
<head>
<meta charset="utf-8">
<title>Space Acquisition: Purchase &amp; Process Deliverables</title>
<link rel="stylesheet" href="https://fonts.googleapis.com/css2?family=Arimo:ital,wght@0,400;0,700;1,400;1,700&display=swap">
<style>
:root{
  --navy:#13294b;
  --wedge-navy:#0f4a75;
  --wedge-light:#7dbde8;
  --wedge-orange:#f15a2c;
  --wedge-red:#d8232f;
  --band-navy:#0c3552;
  --band-blue:#4a90c0;
  --band-orange:#d44a35;
  --band-red:#b3212d;
  --ring:#b8bbbe;
  --step:#8c8c8c;
  --rule:#b5b5b5;
  --ink:#1f1f1f;
  --stage:#d9d9d9;
  --band:#f0f0f0;
}
*{margin:0;padding:0;box-sizing:border-box}
html,body{width:1200px;height:1200px;overflow:hidden;background:var(--stage);font-family:"Arimo",Arial,sans-serif;color:var(--ink)}
.slide{position:absolute;left:182px;width:1350px;height:760px;background:#fff;transform:scale(.6207);transform-origin:0 0;box-shadow:0 4px 10px rgba(0,0,0,.25)}
.slide--one{top:101px}
.slide--two{top:635px}
.slide *{position:absolute}
.slide .inline,.slide span,.slide b,.slide i,.slide u,.slide tspan{position:static}
.title{left:0;right:0;top:28px;text-align:center;font-size:34px;font-weight:400;color:var(--navy);white-space:nowrap}
.title .fig{font-size:19px;font-style:italic;margin-right:8px}
.title b{font-weight:700}
.title-rule{left:57px;width:1236px;top:77px;height:4px;background:var(--navy)}
.col-band{left:57px;width:1236px;top:98px;height:24px;background:var(--band)}
.col-label{top:102px;font-size:14px;color:#8a8a8a;transform:translateX(-50%);white-space:nowrap}
.col-divider{top:98px;height:642px;border-left:1px dashed #e0e0e0}
.wheel{width:520px;height:520px}
.leader{border-color:var(--rule);border-style:solid;border-width:0}
.dot{width:8px;height:8px;border-radius:50%;background:var(--rule);transform:translate(-50%,-50%)}
.step{font-size:24px;font-weight:700;color:var(--step);white-space:nowrap}
.block{font-size:13px;line-height:17px;white-space:nowrap}
.block h4{position:static;font-size:14px;font-weight:700;color:var(--ink)}
.block .bold{font-weight:700;font-size:13px}
.list li{position:static;list-style:none}
.list li::before{content:"• "}
.checks li{position:static;list-style:none;padding-left:18px}
.checks li::before{content:"✓";position:absolute;margin-left:-18px}
.deliv li{position:static;list-style:none}
.deliv .num{font-weight:700;display:inline-block;width:24px}
.deliv .sub{padding-left:28px;font-style:italic}
.deliv .sub::before{content:"• "}
.deliv .gap{margin-top:4px}
.playbooks{font-size:13px;line-height:17px;font-weight:700;font-style:italic;text-align:right;width:140px}
.wheel text{font-family:"Arimo",Arial,sans-serif;font-size:13px;text-anchor:middle}
.wheel .on-dark{fill:#fff}
.wheel .on-light{fill:var(--navy)}
.wheel .strong{font-weight:700}
.wheel .compact{font-size:12px}
.wheel .hub{font-size:22px;font-weight:700;fill:var(--navy)}
.wheel .stage-label{font-size:15px;fill:#333;letter-spacing:.5px}
</style>
</head>
<body>

<!-- ================= SLIDE ONE ================= -->
<section class="slide slide--one">
  <h1 class="title"><span class="fig">FIGURE 5.</span>Space Acquisition: <b>PURCHASE &amp; PROCESS DELIVERABLES</b> (1)</h1>
  <div class="title-rule"></div>
  <div class="col-band"></div>
  <div class="col-label" style="left:234px">Process</div>
  <div class="col-label" style="left:738px">Roles &amp; Responsibilities</div>
  <div class="col-label" style="left:1178px">Deliverables</div>
  <div class="col-divider" style="left:412px"></div>
  <div class="col-divider" style="left:1064px"></div>

  <svg class="wheel" style="left:28px;top:197px" viewBox="-260 -260 520 520" aria-label="Process wheel">
    <g>
      <path fill="var(--wedge-navy)" d="M0 0L0 -238A238 238 0 0 1 139.9 -192.5Z"/>
      <path fill="var(--wedge-navy)" d="M0 0L139.9 -192.5A238 238 0 0 1 226.4 -73.5Z"/>
      <path fill="var(--wedge-navy)" d="M0 0L226.4 -73.5A238 238 0 0 1 226.4 73.5Z"/>
      <path fill="var(--wedge-light)" d="M0 0L226.4 73.5A238 238 0 0 1 139.9 192.5Z"/>
      <path fill="var(--wedge-light)" d="M0 0L139.9 192.5A238 238 0 0 1 0 238Z"/>
      <path fill="var(--wedge-orange)" d="M0 0L0 238A238 238 0 0 1 -139.9 192.5Z"/>
      <path fill="var(--wedge-red)" d="M0 0L-139.9 192.5A238 238 0 0 1 -226.4 73.5Z"/>
      <path fill="var(--wedge-red)" d="M0 0L-226.4 73.5A238 238 0 0 1 -226.4 -73.5Z"/>
      <path fill="var(--wedge-red)" d="M0 0L-226.4 -73.5A238 238 0 0 1 -139.9 -192.5Z"/>
      <path fill="var(--wedge-red)" d="M0 0L-139.9 -192.5A238 238 0 0 1 0 -238Z"/>
    </g>
    <g stroke="#fff" stroke-width="3">
      <line x1="0" y1="0" x2="0" y2="-238"/><line x1="0" y1="0" x2="139.9" y2="-192.5"/>
      <line x1="0" y1="0" x2="226.4" y2="-73.5"/><line x1="0" y1="0" x2="226.4" y2="73.5"/>
      <line x1="0" y1="0" x2="139.9" y2="192.5"/><line x1="0" y1="0" x2="0" y2="238"/>
      <line x1="0" y1="0" x2="-139.9" y2="192.5"/><line x1="0" y1="0" x2="-226.4" y2="73.5"/>
      <line x1="0" y1="0" x2="-226.4" y2="-73.5"/><line x1="0" y1="0" x2="-139.9" y2="-192.5"/>
    </g>
    <g fill="none" stroke-width="13">
      <path stroke="var(--band-navy)" d="M8.6 -245.9A246 246 0 0 1 236.5 67.8"/>
      <path stroke="var(--band-blue)" d="M231.2 84.1A246 246 0 0 1 8.6 245.9"/>
      <path stroke="var(--band-orange)" d="M-8.6 245.9A246 246 0 0 1 -137.6 203.9"/>
      <path stroke="var(--band-red)" d="M-151.5 193.9A246 246 0 0 1 -231.2 84.1"/>
      <path stroke="var(--band-red)" d="M-236.5 67.8A246 246 0 0 1 -151.5 -193.9"/>
      <path stroke="var(--band-red)" d="M-137.6 -203.9A246 246 0 0 1 -8.6 -245.9"/>
    </g>
    <circle r="95" fill="#fff"/>
    <circle r="76" fill="none" stroke="var(--ring)" stroke-width="32"/>
    <g stroke="#fff" stroke-width="4"><line x1="0" y1="-95" x2="0" y2="-55"/><line x1="0" y1="55" x2="0" y2="95"/></g>
    <circle r="59" fill="#fff"/>
    <text class="hub" y="8">PROCESS</text>
    <defs>
      <path id="front-a" d="M23.9 -65.8A70 70 0 0 1 23.9 65.8"/>
      <path id="end-a" d="M-28 -77.1A82 82 0 0 0 -28 77.1"/>
    </defs>
    <text class="stage-label"><textPath href="#front-a" startOffset="50%">FRONTSTAGE</textPath></text>
    <text class="stage-label"><textPath href="#end-a" startOffset="50%">ENDSTAGE</textPath></text>

    <text class="on-dark strong" y="-187"><tspan x="52">Conduct</tspan><tspan x="52" dy="17">Strategic</tspan><tspan x="52" dy="17">Planning</tspan><tspan x="52" dy="17">Define</tspan></text>
    <text class="on-dark strong" y="-104"><tspan x="137">Client</tspan><tspan x="137" dy="17">Requirements</tspan></text>
    <text class="on-dark strong" y="-4"><tspan x="168">Create Budget</tspan><tspan x="168" dy="17">&amp; Schedule</tspan></text>
    <text class="on-light strong" y="88"><tspan x="141">Develop</tspan><tspan x="141" dy="17">Negotiation</tspan><tspan x="141" dy="17">Strategy</tspan></text>
    <text class="on-light strong" y="148"><tspan x="55">Conduct</tspan><tspan x="55" dy="17">Market</tspan><tspan x="55" dy="17">Research</tspan><tspan x="55" dy="17">&amp; Analysis</tspan></text>
    <text class="on-dark" y="155"><tspan x="-55">PERFORMANCE</tspan><tspan x="-55" dy="20">Measure/</tspan><tspan x="-55" dy="17">Demonstrate</tspan><tspan x="-55" dy="17">Performance</tspan></text>
    <text class="on-dark compact" y="50"><tspan x="-98">Develop</tspan><tspan x="-117" dy="14">Move/Project</tspan><tspan x="-135" dy="14">Management</tspan><tspan x="-140" dy="14">Documentation</tspan><tspan x="-143" dy="14">&amp; Transition to</tspan><tspan x="-146" dy="14">Project Manager,</tspan><tspan x="-147" dy="14">if Applicable</tspan></text>
    <text class="on-dark" y="-4"><tspan x="-168">Conduct Due</tspan><tspan x="-168" dy="17">Diligence</tspan></text>
    <text class="on-dark" y="-124"><tspan x="-145">Negotiate/</tspan><tspan x="-145" dy="17">Execute LOI &amp;</tspan><tspan x="-145" dy="17">Purchase &amp; Sale</tspan><tspan x="-145" dy="17">Agreement</tspan></text>
    <text class="on-dark" y="-182"><tspan x="-56">EXECUTION</tspan><tspan x="-56" dy="17">Negotiate with</tspan><tspan x="-56" dy="17">Short List</tspan></text>
  </svg>

  <div class="leader" style="left:381px;top:161px;width:806px;height:66px;border-top-width:2px;border-left-width:2px"></div>
  <div class="dot" style="left:382px;top:227px"></div>
  <div class="leader" style="left:447px;top:519px;width:740px;border-top-width:2px"></div>
  <div class="dot" style="left:447px;top:520px"></div>
  <div class="leader" style="left:339px;top:581px;width:848px;border-top-width:2px"></div>
  <div class="dot" style="left:339px;top:582px"></div>
  <div class="step" style="left:1204px;top:151px">STEP 1</div>
  <div class="step" style="left:1204px;top:509px">STEP 2</div>
  <div class="step" style="left:1204px;top:571px">STEP 3</div>

  <div class="block" style="left:499px;top:197px"><h4>NWC TEAM</h4>
    <ul class="list"><li>Transaction Mgr</li><li>Portfolio Advisor</li><li>Broker</li><li>Project Mgr</li></ul></div>
  <div class="block" style="left:662px;top:197px"><h4>EXTERNAL TEAM</h4>
    <ul class="list"><li>Architect</li><li>Attorney</li><li>General Contractor</li><li>IT Consultant</li></ul></div>
  <div class="block" style="left:662px;top:311px"><h4>CLIENT TEAM</h4>
    <ul class="list"><li>Business Unit Mgr</li><li>Corporate RE Mgr</li><li>Risk Mgr</li><li>Regional Mgr</li><li>Local Operator</li><li>CEO/CFO</li><li>VP of Finance</li><li>Administrator</li><li>Lending Rep</li><li>Tax Advisor</li></ul></div>
  <div class="block" style="left:840px;top:199px">
    <ul class="checks">
      <li>Evaluate requirement in light<br>of client’s strategic plan;<br>develop strategic plan, if<br>appropriate.</li>
      <li style="margin-top:3px">Develop project management<br>strategy, budget, and<br>schedules.</li>
      <li style="margin-top:3px">Review critical action date<br>report monthly.</li>
      <li style="margin-top:3px">Establish KPIs.</li>
      <li style="margin-top:3px">Distribute orientation binder.</li>
      <li style="margin-top:3px">Review existing NWC/Client<br>customized Playbooks for use<br>and applicability.</li>
    </ul></div>
  <div class="block" style="left:1084px;top:197px">
    <ul class="deliv">
      <li><span class="num">1.1</span>Pre-Engagement Documents</li>
      <li class="sub">Authorization Letter</li><li class="sub">Contact List</li><li class="sub">Contracts</li><li class="sub">RFQ Guidance</li><li class="sub">Service Level Agreement (2)</li><li class="sub">Commission Agreement</li><li class="sub">Standard Reporting Templates</li>
      <li class="gap"><span class="num">1.2</span>Client Needs Analysis (2)</li>
      <li style="padding-left:26px;margin-top:2px">Pre-Project Questionnaire</li>
      <li class="gap"><span class="num">1.3</span>Strategic Plan <i>(no deliverable)</i></li>
      <li class="gap"><span class="num">1.4</span>Schedule and Budget</li>
    </ul></div>

  <div class="block" style="left:571px;top:543px"><p class="bold" style="position:static;font-size:14px">Portfolio Advisor, Transaction Manager and/or Broker</p></div>
  <div class="block" style="left:571px;top:621px"><h4>NWC TEAM, CLIENT TEAM, EXTERNAL TEAM</h4>
    <ul class="checks" style="margin-left:11px;margin-top:2px">
      <li>Develop market research comps to determine fair value, market availability,<br>and cost.</li>
      <li style="margin-top:3px">Tour market with client and create shortlist of viable buildings.</li>
      <li style="margin-top:3px">Develop tour list and report to client.</li>
    </ul></div>
  <div class="block" style="left:1084px;top:620px">
    <ul class="deliv">
      <li><span class="num">3.1</span>Market Survey Template</li>
      <li class="gap"><span class="num">3.2</span>Financial Analysis</li>
      <li class="gap"><span class="num">3.3</span>Own vs. Lease Analysis</li>
      <li class="gap"><span class="num">3.4</span>Building Tour Spreadsheet</li>
      <li class="gap"><span class="num">3.5</span>Building Tour Checklist</li>
    </ul></div>
</section>

<!-- ================= SLIDE TWO ================= -->
<section class="slide slide--two">
  <h1 class="title"><span class="fig">FIGURE 5.</span>Space Acquisition: <b>PURCHASE &amp; PROCESS DELIVERABLES</b> (2)</h1>
  <div class="title-rule"></div>
  <div class="col-band"></div>
  <div class="col-label" style="left:328px">Roles &amp; Responsibilities</div>
  <div class="col-label" style="left:769px">Deliverables</div>
  <div class="col-label" style="left:1116px">Process</div>
  <div class="col-divider" style="left:614px"></div>
  <div class="col-divider" style="left:939px"></div>

  <svg class="wheel" style="left:802px;top:196px" viewBox="-260 -260 520 520" aria-label="Process wheel">
    <g>
      <path fill="var(--wedge-navy)" d="M0 0L0 -238A238 238 0 0 1 139.9 -192.5Z"/>
      <path fill="var(--wedge-navy)" d="M0 0L139.9 -192.5A238 238 0 0 1 226.4 -73.5Z"/>
      <path fill="var(--wedge-navy)" d="M0 0L226.4 -73.5A238 238 0 0 1 226.4 73.5Z"/>
      <path fill="var(--wedge-light)" d="M0 0L226.4 73.5A238 238 0 0 1 139.9 192.5Z"/>
      <path fill="var(--wedge-light)" d="M0 0L139.9 192.5A238 238 0 0 1 0 238Z"/>
      <path fill="var(--wedge-orange)" d="M0 0L0 238A238 238 0 0 1 -139.9 192.5Z"/>
      <path fill="var(--wedge-red)" d="M0 0L-139.9 192.5A238 238 0 0 1 -226.4 73.5Z"/>
      <path fill="var(--wedge-red)" d="M0 0L-226.4 73.5A238 238 0 0 1 -226.4 -73.5Z"/>
      <path fill="var(--wedge-red)" d="M0 0L-226.4 -73.5A238 238 0 0 1 -139.9 -192.5Z"/>
      <path fill="var(--wedge-red)" d="M0 0L-139.9 -192.5A238 238 0 0 1 0 -238Z"/>
    </g>
    <g stroke="#fff" stroke-width="3">
      <line x1="0" y1="0" x2="0" y2="-238"/><line x1="0" y1="0" x2="139.9" y2="-192.5"/>
      <line x1="0" y1="0" x2="226.4" y2="-73.5"/><line x1="0" y1="0" x2="226.4" y2="73.5"/>
      <line x1="0" y1="0" x2="139.9" y2="192.5"/><line x1="0" y1="0" x2="0" y2="238"/>
      <line x1="0" y1="0" x2="-139.9" y2="192.5"/><line x1="0" y1="0" x2="-226.4" y2="73.5"/>
      <line x1="0" y1="0" x2="-226.4" y2="-73.5"/><line x1="0" y1="0" x2="-139.9" y2="-192.5"/>
    </g>
    <g fill="none" stroke-width="13">
      <path stroke="var(--band-navy)" d="M8.6 -245.9A246 246 0 0 1 236.5 67.8"/>
      <path stroke="var(--band-blue)" d="M231.2 84.1A246 246 0 0 1 8.6 245.9"/>
      <path stroke="var(--band-orange)" d="M-8.6 245.9A246 246 0 0 1 -137.6 203.9"/>
      <path stroke="var(--band-red)" d="M-151.5 193.9A246 246 0 0 1 -231.2 84.1"/>
      <path stroke="var(--band-red)" d="M-236.5 67.8A246 246 0 0 1 -151.5 -193.9"/>
      <path stroke="var(--band-red)" d="M-137.6 -203.9A246 246 0 0 1 -8.6 -245.9"/>
    </g>
    <circle r="95" fill="#fff"/>
    <circle r="76" fill="none" stroke="var(--ring)" stroke-width="32"/>
    <g stroke="#fff" stroke-width="4"><line x1="0" y1="-95" x2="0" y2="-55"/><line x1="0" y1="55" x2="0" y2="95"/></g>
    <circle r="59" fill="#fff"/>
    <text class="hub" y="8">PROCESS</text>
    <defs>
      <path id="front-b" d="M23.9 -65.8A70 70 0 0 1 23.9 65.8"/>
      <path id="end-b" d="M-28 -77.1A82 82 0 0 0 -28 77.1"/>
    </defs>
    <text class="stage-label"><textPath href="#front-b" startOffset="50%">FRONTSTAGE</textPath></text>
    <text class="stage-label"><textPath href="#end-b" startOffset="50%">ENDSTAGE</textPath></text>

    <text class="on-dark" y="-187"><tspan x="52">Conduct</tspan><tspan x="52" dy="16">Strategic</tspan><tspan x="52" dy="16">Planning</tspan><tspan x="52" dy="16">Define</tspan></text>
    <text class="on-dark" y="-104"><tspan x="137">Client</tspan><tspan x="137" dy="16">Requirements</tspan></text>
    <text class="on-dark" y="-4"><tspan x="168">Create Budget</tspan><tspan x="168" dy="16">&amp; Schedule</tspan></text>
    <text class="on-dark" y="88"><tspan x="141">Develop</tspan><tspan x="141" dy="16">Negotiation</tspan><tspan x="141" dy="16">Strategy</tspan></text>
    <text class="on-dark" y="148"><tspan x="55">Conduct</tspan><tspan x="55" dy="16">Market</tspan><tspan x="55" dy="16">Research</tspan><tspan x="55" dy="16">&amp; Analysis</tspan></text>
    <text class="on-dark strong" y="155"><tspan x="-55">PERFORMANCE</tspan><tspan x="-55" dy="20">Measure/</tspan><tspan x="-55" dy="17">Demonstrate</tspan><tspan x="-55" dy="17">Performance</tspan></text>
    <text class="on-dark strong compact" y="50"><tspan x="-98">Develop</tspan><tspan x="-117" dy="14">Move/Project</tspan><tspan x="-135" dy="14">Management</tspan><tspan x="-140" dy="14">Documentation</tspan><tspan x="-143" dy="14">&amp; Transition to</tspan><tspan x="-146" dy="14">Project Manager,</tspan><tspan x="-147" dy="14">if Applicable</tspan></text>
    <text class="on-dark strong" y="-4"><tspan x="-168">Conduct Due</tspan><tspan x="-168" dy="17">Diligence</tspan></text>
    <text class="on-dark strong" y="-124"><tspan x="-145">Negotiate/</tspan><tspan x="-145" dy="17">Execute LOI &amp;</tspan><tspan x="-145" dy="17">Purchase &amp; Sale</tspan><tspan x="-145" dy="17">Agreement</tspan></text>
    <text class="on-dark strong" y="-182"><tspan x="-56">EXECUTION</tspan><tspan x="-56" dy="17">Negotiate with</tspan><tspan x="-56" dy="17">Short List</tspan></text>
  </svg>

  <div class="leader" style="left:163px;top:164px;width:861px;height:74px;border-top-width:2px;border-right-width:2px"></div>
  <div class="dot" style="left:1023px;top:238px"></div>
  <div class="leader" style="left:163px;top:250px;width:733px;height:58px;border-top-width:2px;border-right-width:2px"></div>
  <div class="dot" style="left:895px;top:308px"></div>
  <div class="leader" style="left:163px;top:319px;width:685px;height:64px;border-top-width:2px;border-right-width:2px"></div>
  <div class="dot" style="left:847px;top:383px"></div>
  <div class="leader" style="left:163px;top:444px;width:605px;height:97px;border-top-width:2px;border-right-width:2px"></div>
  <div class="leader" style="left:767px;top:539px;width:88px;border-top-width:2px"></div>
  <div class="dot" style="left:855px;top:540px"></div>
  <div class="leader" style="left:163px;top:611px;width:809px;border-top-width:2px"></div>
  <div class="dot" style="left:972px;top:612px"></div>

  <div class="step" style="left:61px;top:151px">STEP 4</div>
  <div class="step" style="left:61px;top:237px">STEP 5</div>
  <div class="step" style="left:61px;top:306px">STEP 6</div>
  <div class="step" style="left:61px;top:431px">STEP 7</div>
  <div class="step" style="left:61px;top:599px">STEP 8</div>

  <div class="block" style="left:61px;top:185px"><p class="bold" style="position:static">Portfolio Advisor, Transaction Manager and/or Broker</p>
    <ul class="checks" style="margin-left:11px;margin-top:3px"><li>Orchestrate competition.</li></ul></div>
  <div class="block" style="left:61px;top:272px"><p class="bold" style="position:static">Portfolio Advisor, Transaction Manager and/or Broker</p></div>
  <div class="block" style="left:61px;top:342px"><p class="bold" style="position:static">Portfolio Advisor, Transaction Manager and/or Broker, Tax Specialist, Lender Rep,<br>Client Legal, Client Risk, Third Party Vendors</p>
    <ul class="checks" style="margin-left:11px;margin-top:3px"><li>Due diligence may include environmental, structural, A&amp;E, title, clarity, appraisal,<br>financial appraisal, tax implications, etc.</li></ul></div>
  <div class="block" style="left:61px;top:466px"><p class="bold" style="position:static">Portfolio Advisor, Transaction Manager and/or Broker, Project Manager, Relocation<br>Manager, Lease Administrator</p>
    <ul class="checks" style="margin-left:11px;margin-top:3px">
      <li>Transaction manager brings in other service line experts (project management, lease<br>administration), if appropriate.</li>
      <li style="margin-top:3px">If NWC is performing project mgmt, see PM Playbook.</li>
      <li style="margin-top:3px">If NWC is <u>not</u> performing project mgmt, coordinate with client representative or landlord.</li>
    </ul></div>
  <div class="block" style="left:61px;top:636px"><p class="bold" style="position:static">Portfolio Advisor, Transaction Manager and/or Broker</p>
    <ul class="checks" style="margin-left:11px;margin-top:3px">
      <li>Benchmark performance and KPIs.</li>
      <li style="margin-top:3px">Submit client satisfaction forms.</li>
      <li style="margin-top:3px">Complete close-out summaries and corresponding critical date reports.</li>
      <li style="margin-top:3px">Create client case study, if transaction size meets criteria.</li>
    </ul></div>

  <div class="block" style="left:638px;top:272px"><ul class="deliv">
    <li><span class="num">5.1</span>Letter of Intent</li><li class="gap"><span class="num">5.2</span>Purchase and Sale Agreement</li></ul></div>
  <div class="block" style="left:638px;top:344px"><ul class="deliv">
    <li><span class="num">6.1</span>Closing Checklist</li><li class="gap"><span class="num">6.2</span>Due Diligence Checklist</li></ul></div>
  <p class="playbooks" style="left:612px;top:456px">See Project<br>Management and<br>Facilities<br>Management<br>Playbooks</p>
  <div class="block" style="left:638px;top:636px"><ul class="deliv">
    <li><span class="num">8.1</span>KPI Documentation</li>
    <li class="gap"><span class="num">8.2</span>Client Survey</li>
    <li class="gap"><span class="num">8.3</span>Close-Out Package</li>
    <li class="gap"><span class="num">8.4</span>Value-Added Matrix and Scorecard</li></ul></div>
</section>

</body>
</html>
```